Luggage and travel essentials company needs Letterhead design (including logo)

Brambury luggage is a travel retailer focussed on selling luggage and travel essentials.
We are a company that have a traditional approach to customer service and also embraces the latest technology, especially where it improves the customer experience.
I would like the design to have an airport hint (airport imagery and font preferred), I would also like the colour blue to feature heavily (see attached image for colour hint).
The final design should aim to give the customer confidence that we are dependable and reliable (no script fonts or crazy colours please) but also reflect that we are an innovative and technology focused company.
I would like the letterhead design to include a logo and text.
I am interested in letterhead text containing an embedded logo (much like the 'Z' in Zephyra's logo is also used separately) Note: this is optional.
The text of the letterhead should include the words "Brambury Luggage & Travel Essentials", and should include a space for the company phone number, email address, website address along with the company physical address.
Target Market(s)
Affluent Adults aged 25 years and above - Predominantly female
Industry/Entity Type
Airport

```html
<!DOCTYPE html>
<html lang="en">
<head>
<meta charset="utf-8">
<title>Brambury Luggage &amp; Travel Essentials — Stationery</title>
<link rel="stylesheet" href="https://fonts.googleapis.com/css2?family=Raleway:wght@400;500&display=swap">
<style>
  :root {
    --brand-blue: #1f9ad8;
    --paper: #ffffff;
    --backdrop: #ffffff;
    --rule: #d9dde1;
    --ink-soft: #3a8fc4;
    --shadow: rgba(0, 0, 0, 0.18);
  }
  * { box-sizing: border-box; margin: 0; padding: 0; }
  html, body {
    width: 896px; height: 1200px; overflow: hidden;
    background: var(--backdrop);
    font-family: "Raleway", Arial, sans-serif;
  }
  .stationery { position: relative; width: 896px; height: 1200px; }

  /* Wordmark: invented name, single line, one colour and weight */
  .brand {
    display: flex; align-items: center; gap: 12px;
    color: var(--brand-blue); font-weight: 500;
    text-transform: uppercase; letter-spacing: 0.08em; white-space: nowrap;
  }
  .brand-mark { width: 14px; height: 14px; background: var(--brand-blue); flex: none; }
  .brand-name { line-height: 1; }

  /* Letterhead sheet */
  .letterhead {
    position: absolute; left: 45px; top: 15px; width: 810px; height: 1170px;
    background: var(--paper);
    border: 1px solid var(--rule);
    box-shadow: 0 2px 8px var(--shadow);
  }
  .letterhead .brand { position: absolute; left: 40px; top: 70px; font-size: 18px; }

  .letterhead-footer {
    position: absolute; left: 40px; bottom: 42px;
    color: var(--ink-soft); font-size: 13px; line-height: 1.55;
  }
  .footer-badge {
    width: 26px; height: 26px; border-radius: 50%;
    border: 2px solid var(--brand-blue); margin-bottom: 12px;
  }
  .footer-web { margin-top: 28px; }

  /* Envelope, reverse side */
  .envelope-back {
    position: absolute; left: 135px; top: 420px; width: 690px; height: 200px;
    background: var(--paper);
    box-shadow: 0 3px 10px var(--shadow);
    transform: rotate(-3deg);
    overflow: hidden;
  }
  .envelope-flap { position: absolute; inset: 0 0 auto 0; height: 165px; }
  .flap-text {
    position: absolute; left: 78px; top: 22px;
    color: var(--paper); font-size: 12px; line-height: 1.6;
  }
  .flap-web { margin-top: 20px; }
  .flap-badge {
    position: absolute; right: 40px; top: 62px; width: 26px; height: 26px;
    border-radius: 50%; border: 2px solid var(--paper);
  }

  /* Envelope, front side */
  .envelope-front {
    position: absolute; left: 126px; top: 592px; width: 690px; height: 262px;
    background: var(--paper);
    box-shadow: 0 3px 12px var(--shadow);
    transform: rotate(-3deg);
  }
  .envelope-front .brand { position: absolute; left: 48px; top: 128px; font-size: 14px; gap: 10px; }
  .envelope-front .brand-mark { width: 11px; height: 11px; }
</style>
</head>
<body>
<main class="stationery">

  <section class="letterhead" aria-label="Letterhead">
    <div class="brand">
      <span class="brand-mark"></span>
      <span class="brand-name">Brambury Luggage &amp; Travel Essentials</span>
    </div>
    <footer class="letterhead-footer">
      <div class="footer-badge"></div>
      <p>Kent TN12 4QR, United Kingdom</p>
      <p>Phone: +44 800 555 0147, Fax: +44 800 555 0148</p>
      <p>Email: info@bramburyluggage.uk</p>
      <p class="footer-web">www.bramburyluggage.uk</p>
    </footer>
  </section>

  <section class="envelope-back" aria-label="Envelope reverse">
    <svg class="envelope-flap" viewBox="0 0 690 165" preserveAspectRatio="none" aria-hidden="true">
      <polygon points="0,0 690,0 690,150 345,165 0,150" fill="var(--brand-blue)"/>
    </svg>
    <div class="flap-text">
      <p>Kent TN12 4QR, United Kingdom</p>
      <p>Phone: +44 800 555 0147, Fax: +44 800 555 0148</p>
      <p>Email: info@bramburyluggage.uk</p>
      <p class="flap-web">www.bramburyluggage.uk</p>
    </div>
    <div class="flap-badge"></div>
  </section>

  <section class="envelope-front" aria-label="Envelope front">
    <div class="brand">
      <span class="brand-mark"></span>
      <span class="brand-name">Brambury Luggage &amp; Travel Essentials</span>
    </div>
  </section>

</main>
</body>
</html>
```